Harlow Ridge Partners Business Cards

Design Business cards in a format where I can change the information and utilize a third party buisness card printing company

Contact Information for Business Card

Want Logo and Name on Back. Looking for Spot UV style shine on Logo. Probably Black background. Want smaller logo on front with contact details. Like rounded edges or something else interesting.

Requirements
Must have
• Strong masculine look.

```html
<!DOCTYPE html>
<html lang="en">
<head>
<meta charset="utf-8">
<title>Harlow Ridge Partners – Business Cards</title>
<link href="https://fonts.googleapis.com/css2?family=Cinzel:wght@400;500&family=Arimo:wght@400&display=swap" rel="stylesheet">
<style>
  :root {
    --backdrop: #2b2b2b;
    --card: #0b0b0b;
    --card-edge: #1a1a1a;
    --silver-bright: #e6e6e6;
    --silver: #a9a9a9;
    --silver-dim: #7d7d7d;
    --rule: #3a3a3a;
  }
  * { box-sizing: border-box; margin: 0; padding: 0; }
  html, body {
    width: 1200px; height: 782px; overflow: hidden;
    background: var(--backdrop);
  }
  .canvas { position: relative; width: 1200px; height: 782px; }

  .card {
    position: absolute;
    width: 560px; height: 320px;
    background: var(--card);
    border: 1px solid var(--card-edge);
    border-radius: 6px;
    box-shadow: 0 14px 30px rgba(0,0,0,.45);
  }

  /* Back card: name mark + website */
  .card-back { left: 560px; top: 60px; }
  .back-square {
    position: absolute; left: 254px; top: 62px;
    width: 52px; height: 52px;
    background: var(--silver-bright);
  }
  .back-mark {
    position: absolute; left: 0; right: 0; top: 136px;
    text-align: center; white-space: nowrap;
    font-family: "Cinzel", serif; font-weight: 500;
    font-size: 32px; letter-spacing: 2px;
    color: var(--silver-bright);
  }
  .back-url {
    position: absolute; left: 0; right: 0; top: 240px;
    text-align: center;
    font-family: "Cinzel", serif; font-size: 14px; letter-spacing: 1.5px;
    color: var(--silver-dim);
  }

  /* Front card: contact details + name mark */
  .card-front { left: 80px; top: 410px; }
  .person { position: absolute; left: 40px; top: 62px; }
  .person-name {
    font-family: "Cinzel", serif; font-size: 19px; letter-spacing: 1px;
    color: var(--silver);
  }
  .person-role {
    font-family: "Arimo", sans-serif; font-size: 12px;
    color: var(--silver-dim); margin-top: 2px;
  }
  .contact-list { list-style: none; margin-top: 10px; }
  .contact-list li {
    display: flex; align-items: center; gap: 8px;
    font-family: "Arimo", sans-serif; font-size: 12.5px;
    color: var(--silver); line-height: 19px;
  }
  .contact-list svg { width: 10px; height: 10px; fill: var(--silver-dim); flex: none; }

  .front-square {
    position: absolute; right: 36px; top: 70px;
    width: 32px; height: 32px;
    background: var(--silver);
  }
  .front-mark {
    position: absolute; right: 36px; top: 116px;
    text-align: right; white-space: nowrap;
    font-family: "Cinzel", serif; font-size: 20px; letter-spacing: 1px;
    color: var(--silver);
  }
  .front-rule {
    position: absolute; left: 240px; right: 36px; top: 160px;
    height: 1px; background: var(--rule);
  }
  .front-rule.lower { left: 300px; top: 224px; }
  .address {
    position: absolute; right: 36px; top: 238px; text-align: right;
    font-family: "Arimo", sans-serif; font-size: 13px; line-height: 18px;
    color: var(--silver);
  }
</style>
</head>
<body>
<main class="canvas">

  <section class="card card-back" aria-label="Business card, back">
    <div class="back-square" aria-hidden="true"></div>
    <div class="back-mark">Harlow Ridge Partners</div>
    <div class="back-url">www.harlowridgepartners.com</div>
  </section>

  <section class="card card-front" aria-label="Business card, front">
    <div class="person">
      <div class="person-name">DORIAN VALE</div>
      <div class="person-role">Managing Director</div>
      <ul class="contact-list">
        <li>
          <svg viewBox="0 0 10 10" aria-hidden="true"><path d="M1 3.5C1 2 2 1 3.5 1h3C8 1 9 2 9 3.5L7.5 4.5 6.5 3h-3L2.5 4.5zM2 6h6l1 3H1z"/></svg>
          021-480 735 612
        </li>
        <li>
          <svg viewBox="0 0 10 10" aria-hidden="true"><path d="M3 0h4a1 1 0 0 1 1 1v8a1 1 0 0 1-1 1H3a1 1 0 0 1-1-1V1a1 1 0 0 1 1-1zm0 1.5v6h4v-6z"/></svg>
          021-480 735 612
        </li>
        <li>
          <svg viewBox="0 0 10 10" aria-hidden="true"><path d="M0 2h10v6H0zm1 1v.4l4 2.6 4-2.6V3z"/></svg>
          hello@harlowridge.co
        </li>
        <li>
          <svg viewBox="0 0 10 10" aria-hidden="true"><path d="M5 0a5 5 0 1 1 0 10A5 5 0 0 1 5 0zm0 1.2a3.8 3.8 0 1 0 0 7.6 3.8 3.8 0 0 0 0-7.6zM1.5 4.5h7v1h-7z"/></svg>
          www.harlowridge.co
        </li>
      </ul>
    </div>

    <div class="front-square" aria-hidden="true"></div>
    <div class="front-mark">Harlow Ridge Partners</div>
    <div class="front-rule"></div>
    <div class="front-rule lower"></div>
    <div class="address">48 Kestrel Yard, Millbank Row<br>Northwold, 540218</div>
  </section>

</main>
</body>
</html>
```